Podcast Art for Bright Belly Days: Rising above Crohn's Colitis

Read carefully Please. Most submittals so far have not read this.

We're looking for stunning, eye-catching, innovative yet simple podcast art for our first Podcast

Background should be solid, one color

Bright Belly Days: Rising above Crohn's Colitis
with Marcus Delvanto

Use our Brand Guide including logo, colors, and font
https://lnk.example-short.net/BBD2020BrandGuide

Some Podcast Covers I like: https://casts.tunewaveaudio.net/

Optional: Mega Flusher graphic included above and/or my headshot uploaded below

As you can see humor / medutainment is part of the brand. As we are talking serious topic such as a disease many suffer from you can see the humor in the logo and "mega flusher" . Here is the monologue for the first episode to give you a deeper feel on the content

https://files.paperdeskcloud.net/doc/7qR_Km2LpX9vTzB4nWcYhA31EoUfJsDiGkPeVbNr/view?share=link

Target Market(s)

Those who suffer from gut issues, are diagnosed with inflammatory bowel disease(IBD), Crohn's Disease or Ulcerative Colitis - also their coaches, doctors, practitioners so functional or integrative medicine doctors/coaches, gastroenterologists etc.

Industry/Entity Type

Health And Wellness

Font styles to use
Other font styles liked:
• Primary: Oswald bold. Secondary: Oswald Medium or light

Requirements
Must have
• 3000 x 3000 pixels
Simple and eye-catching
Brand Guide Logo
Brand Guide Font
Brand Guide Colors including accent color(s)
I did not select colors below because I have included our Brand guide. Please use the exact colors there.
Nice to have
• Maybe my headshot and/or the mega flusher graphic - if not too busy and still looks good
Should not have
• - Look busy
- Reverse Logo
- Not follow the Brand Guide
- Anything in the background but one solid color from the brief

```html
<!DOCTYPE html>
<html lang="en">
<head>
<meta charset="utf-8">
<title>Bright Belly Days: Rising above Crohn's Colitis – Podcast Cover</title>
<link rel="stylesheet" href="https://fonts.googleapis.com/css2?family=Oswald:wght@500;600;700&display=swap">
<style>
  :root {
    --brand-orange: #f26a3f;
    --brand-navy: #233a8c;
    --canvas-light: #ececec;
    --canvas-mid: #dcdcdc;
    --photo-warm: #e98a62;
    --photo-shirt: #f6f3ef;
  }
  * { margin: 0; padding: 0; box-sizing: border-box; }
  html, body { width: 1200px; height: 1200px; overflow: hidden; background: #fff; }
  .cover {
    position: relative;
    width: 1200px;
    height: 1200px;
    background: radial-gradient(circle at 50% 45%, var(--canvas-light) 0%, var(--canvas-mid) 100%);
    border: 10px solid var(--brand-navy);
    font-family: "Oswald", "Arial Narrow", sans-serif;
    overflow: hidden;
  }
  .host-photo {
    position: absolute;
    left: 360px; top: 28px;
    width: 458px; height: 416px;
    background:
      radial-gradient(ellipse 42% 48% at 52% 42%, rgba(233, 138, 98, 0.55) 0%, rgba(233, 138, 98, 0) 100%),
      linear-gradient(180deg,
        var(--brand-orange) 0%,
        var(--brand-orange) 58%,
        var(--photo-warm) 70%,
        var(--photo-shirt) 82%,
        var(--photo-shirt) 100%);
  }
  .frame-line { position: absolute; background: var(--brand-navy); }
  .frame-top-left     { left: 40px;  top: 248px; width: 302px; height: 2px; }
  .frame-top-right    { left: 837px; top: 248px; width: 305px; height: 2px; }
  .frame-left         { left: 40px;  top: 248px; width: 2px;  height: 528px; }
  .frame-right        { left: 1140px; top: 248px; width: 2px; height: 528px; }
  .frame-bottom-left  { left: 40px;  top: 774px; width: 332px; height: 2px; }
  .frame-bottom-right { left: 818px; top: 774px; width: 324px; height: 2px; }

  .show-title {
    position: absolute;
    left: 0; right: 0; top: 472px;
    text-align: center;
    font-weight: 700;
    font-style: italic;
    font-size: 108px;
    line-height: 1;
    letter-spacing: 1px;
    text-transform: uppercase;
    color: var(--brand-navy);
    white-space: nowrap;
  }
  .show-title .accent { color: var(--brand-orange); }
  .show-tagline {
    position: absolute;
    left: 0; right: 0; top: 616px;
    text-align: center;
    font-weight: 700;
    font-style: italic;
    font-size: 84px;
    line-height: 1;
    letter-spacing: 2px;
    text-transform: uppercase;
    color: var(--brand-navy);
  }
  .title-rule {
    position: absolute;
    left: 446px; top: 722px;
    width: 308px; height: 2px;
    background: var(--brand-navy);
  }
  .show-credit {
    position: absolute;
    left: 0; right: 0; top: 738px;
    text-align: center;
    font-weight: 600;
    font-style: italic;
    font-size: 33px;
    line-height: 1.45;
    letter-spacing: 1px;
    text-transform: uppercase;
    color: var(--brand-navy);
  }
  .mascot {
    position: absolute;
    left: 420px; top: 874px;
    width: 166px; height: 290px;
    background: linear-gradient(180deg, #2c4596 0%, var(--brand-navy) 100%);
    border-radius: 60px 60px 18px 18px;
  }
  .brand-mark {
    position: absolute;
    left: 630px; top: 902px;
    width: 150px; height: 262px;
    display: flex;
    flex-direction: column;
    align-items: center;
    justify-content: center;
    gap: 14px;
  }
  .brand-mark-dot {
    width: 34px; height: 34px;
    border-radius: 50%;
    background: var(--brand-navy);
  }
  .brand-mark-name {
    font-weight: 700;
    font-size: 44px;
    line-height: 1.02;
    text-align: center;
    text-transform: uppercase;
    color: var(--brand-navy);
  }
</style>
</head>
<body>
  <main class="cover">
    <div class="frame-line frame-top-left"></div>
    <div class="frame-line frame-top-right"></div>
    <div class="frame-line frame-left"></div>
    <div class="frame-line frame-right"></div>
    <div class="frame-line frame-bottom-left"></div>
    <div class="frame-line frame-bottom-right"></div>

    <div class="host-photo" role="img" aria-label="Headshot of host Marcus Delvanto smiling in a white shirt on an orange background"></div>

    <h1 class="show-title"><span class="accent">Bright Belly</span> Days:</h1>
    <p class="show-tagline">Rising Above</p>
    <div class="title-rule"></div>
    <p class="show-credit">Crohn's Colitis<br>with Marcus Delvanto</p>

    <div class="mascot" role="img" aria-label="Mega Flusher superhero mascot figure with a cape, in navy"></div>

    <div class="brand-mark" aria-label="Bright Belly Days logo">
      <span class="brand-mark-dot"></span>
      <span class="brand-mark-name">Bright<br>Belly<br>Days</span>
    </div>
  </main>
</body>
</html>
```